Design my site www.marquetally.example

So here is what I am thinking in terms of design:

https://plovex.example

https://www.caldorejet.example

http://brevon.example/harbor-spire-plaza/

I want the theme to be white and blue (royal blue). I attached a paint picture of what I would like the site to look like in terms of placing the text. Generally, what I like about the sites above is that they are simple, you can navigate easily and have some kind of idea of what's going on by looking at the center (picture and motto). Let's establish a clear understanding of how the functional part of the site would look like. Please see the picture attached.

I want to keep it simple: On top would be the Name 'MARQUE tally", somewhere to the right on top on the page would be 'Sign in" button.

In the center would be a picture (maybe a video) with the Motto (on top of it all in capital) OBSERVE NAVIGATE DECIDE and below would be the "sign up now"

Below the picture (like on brevon.example site) or to the left on top of the page would be "About Us', "Press" "Contact Us' buttons.

Then once the user gets to his page his got 3 tabs " Press Headlines", "Events", " Briefings".

we would keep the same format I only have on the site, but separate for every Tab.

I do not want the user to get distracted. I also want him to be able to access the page though mobile phone and be able to get automatic updates just like Fennix Pings without having to sign in daily.

The landing page must be minimalist yet with business/corporate feel where users can navigate easily and a "what you see is what you get" approach. You want an image or video (personally I prefer the video.. it does capture the users attention instantly, as long as it is an interesting video), with your taglines in it.

Sections available to public: About Us, Contact Us, Landing Page with Signup Option

Private: Public Sections + User Account Page, Tabs for (Events, Press Headlines, Briefings)

Target Market(s)

PR/media monitoring/diplomatic community

Coding

Coded - Design and coding required

Number of Pages Required

1 page

Font styles to use
Serif
Sans Serif

Colors
0255a3
ec1f27

Requirements
Must have
• a simple landing page, that is user friendly.
Nice to have
• a video with the explanation of how to navigate the site
Should not have
• too many colors, graphs etc.

```html
<!DOCTYPE html>
<html lang="en">
<head>
<meta charset="utf-8">
<title>MARQUE tally</title>
<link rel="stylesheet" href="https://fonts.googleapis.com/css2?family=Josefin+Sans:wght@300;400&family=Nunito+Sans:wght@600;700;800&family=Open+Sans:wght@300;400&display=swap">
<style>
  :root {
    --white: #ffffff;
    --line: rgba(255, 255, 255, 0.75);
    --header-band: rgba(20, 45, 62, 0.55);
    --sky-top: #2b4a5d;
    --sky-mid: #8c7d72;
    --sky-warm: #c39a76;
    --city-mid: #8a6a52;
    --city-low: #4d3a2e;
    --accent: #ff0a84;
    --accent-soft: rgba(214, 30, 120, 0.55);
    --accent-edge: rgba(255, 150, 200, 0.6);
  }
  * { box-sizing: border-box; margin: 0; padding: 0; }
  html, body { width: 1200px; height: 562px; overflow: hidden; }
  body { font-family: "Open Sans", sans-serif; color: var(--white); }

  .landing { position: relative; width: 1200px; height: 562px; overflow: hidden; }

  .hero-photo {
    position: absolute; inset: 0;
    background: linear-gradient(180deg,
      var(--sky-top) 0%,
      #4f5f66 22%,
      var(--sky-mid) 40%,
      var(--sky-warm) 55%,
      var(--city-mid) 72%,
      var(--city-low) 100%);
  }

  .site-header {
    position: absolute; top: 0; left: 0; right: 0; height: 54px;
    background: var(--header-band);
  }
  .brand {
    position: absolute; left: 162px; top: 13px;
    font-family: "Josefin Sans", sans-serif; font-weight: 400;
    font-size: 26px; line-height: 28px; letter-spacing: 1px;
    color: var(--white);
  }
  .header-signup {
    position: absolute; left: 956px; top: 13px; width: 82px; height: 28px;
    border: 1.5px solid var(--white); border-radius: 14px;
    font-family: "Nunito Sans", sans-serif; font-weight: 800;
    font-size: 10px; letter-spacing: 0.5px;
    display: flex; align-items: center; justify-content: center;
    color: var(--white); text-decoration: none;
  }

  .hero-title {
    position: absolute; left: 0; right: 0; top: 128px; text-align: center;
    font-family: "Josefin Sans", sans-serif; font-weight: 300;
    font-size: 54px; line-height: 60px; letter-spacing: 4px;
    text-transform: uppercase; color: var(--white);
  }
  .motto {
    position: absolute; left: 346px; width: 509px; top: 207px; height: 50px;
    border-top: 1px solid var(--line); border-bottom: 1px solid var(--line);
    display: flex; align-items: center; justify-content: center;
    font-weight: 300; font-size: 27px; letter-spacing: 0.3px;
  }
  .signup-now {
    position: absolute; left: 484px; top: 296px; width: 232px; height: 54px;
    border: 1px solid var(--line);
    display: flex; align-items: center; justify-content: center; gap: 6px;
    font-family: "Nunito Sans", sans-serif; font-weight: 800;
    font-size: 21px; letter-spacing: 0.3px; color: var(--white); text-decoration: none;
  }
  .signup-now svg { width: 12px; height: 10px; }

  .section-nav { position: absolute; left: 250px; top: 494px; display: flex; gap: 7px; }
  .section-link {
    width: 229px; height: 68px; padding-bottom: 8px;
    display: flex; align-items: center; justify-content: center;
    font-family: "Nunito Sans", sans-serif; font-weight: 700;
    font-size: 19px; text-transform: uppercase; color: var(--white); text-decoration: none;
    background: var(--accent-soft); border: 1px solid var(--accent-edge); border-bottom: none;
  }
  .section-link.is-active { background: var(--accent); border-color: var(--accent); }
</style>
</head>
<body>
<main class="landing">
  <div class="hero-photo" role="img" aria-label="Aerial photograph of a city skyline at sunset with a tall spire tower in the centre and a harbour behind"></div>

  <header class="site-header">
    <div class="brand">MT</div>
    <a class="header-signup" href="#">SIGN UP</a>
  </header>

  <h1 class="hero-title">MARQUE tally</h1>
  <p class="motto">Observe Navigate Decide</p>
  <a class="signup-now" href="#">SIGNUP NOW
    <svg viewBox="0 0 12 10" aria-hidden="true"><path d="M0 5h9M6 1.5L10 5 6 8.5" fill="none" stroke="#fff" stroke-width="2"/></svg>
  </a>

  <nav class="section-nav">
    <a class="section-link is-active" href="#">About Us</a>
    <a class="section-link" href="#">Press</a>
    <a class="section-link" href="#">Contact</a>
  </nav>
</main>
</body>
</html>
```